Copper wren builds

Copper wren builds is a small construction company.
Who is a licenced builder, Carpenter, joiner,
working on heritage ,new build, speacial projects and sometimes furniture

Industry/Entity Type

Construction

```html
<!DOCTYPE html>
<html lang="en">
<head>
<meta charset="utf-8">
<title>Copper wren builds — Business Card</title>
<link href="https://fonts.googleapis.com/css2?family=Montserrat:wght@400;500;800&display=swap" rel="stylesheet">
<style>
  :root {
    --stage: #d9dbd6;
    --card-black: #0b0b0b;
    --card-charcoal: #262626;
    --green-bright: #55a016;
    --green-deep: #3a7410;
    --text-light: #f2f2f2;
  }
  * { margin: 0; padding: 0; box-sizing: border-box; }
  html, body { width: 1200px; height: 1000px; overflow: hidden; }
  body {
    background: var(--stage);
    font-family: "Montserrat", Arial, sans-serif;
    display: flex; align-items: center; justify-content: center;
  }
  .card {
    position: relative;
    width: 1000px; height: 580px;
    border-radius: 34px;
    overflow: hidden;
    background: radial-gradient(ellipse at 45% 25%, var(--card-charcoal) 0%, var(--card-black) 65%);
    box-shadow: 0 18px 40px rgba(0,0,0,.35);
  }
  .card__shapes { position: absolute; inset: 0; }
  .brand {
    position: absolute; left: 62px; top: 124px;
    font-weight: 800; font-size: 38px; letter-spacing: 1px;
    color: var(--green-bright); text-transform: uppercase;
    line-height: 1; white-space: nowrap;
  }
  .holder { position: absolute; left: 80px; top: 278px; }
  .holder__name { font-weight: 800; font-size: 34px; color: var(--green-bright); }
  .holder__role { font-weight: 500; font-size: 19px; color: var(--text-light); margin-top: 4px; }
  .address {
    position: absolute; right: 70px; top: 200px;
    text-align: right; color: var(--text-light);
    font-size: 23px; line-height: 1.35; font-style: normal;
  }
  .contacts { position: absolute; left: 110px; top: 400px; list-style: none; }
  .contacts__item {
    display: flex; align-items: center; gap: 16px;
    color: var(--text-light); font-size: 27px; height: 40px;
  }
  .contacts__icon { width: 24px; height: 24px; flex: none; }
</style>
</head>
<body>
  <article class="card">
    <svg class="card__shapes" viewBox="0 0 1000 580" width="1000" height="580" aria-hidden="true">
      <line x1="650" y1="160" x2="945" y2="160" stroke="var(--green-bright)" stroke-width="3"/>
      <line x1="72" y1="360" x2="410" y2="360" stroke="var(--green-bright)" stroke-width="3"/>
      <path d="M600,580 V405 Q600,372 635,372 H1000 V580 Z" fill="var(--green-bright)"/>
      <path d="M575,580 V440 Q575,408 610,408 H1000 V580 Z" fill="var(--green-deep)"/>
      <path d="M0,528 H560 Q570,528 575,518 V580 H0 Z" fill="var(--green-deep)"/>
      <path d="M0,536 H1000 V544 H0 Z" fill="var(--card-black)"/>
      <path d="M0,546 H1000 V580 H0 Z" fill="var(--green-bright)"/>
    </svg>

    <div class="brand">Copper wren builds</div>

    <div class="holder">
      <div class="holder__name">Mara Holt</div>
      <div class="holder__role">Licenced Builder &amp; Carpenter</div>
    </div>

    <address class="address">
      Your Street Address Here<br>Singapore 56789
    </address>

    <ul class="contacts">
      <li class="contacts__item">
        <svg class="contacts__icon" viewBox="0 0 24 24" aria-hidden="true">
          <circle cx="12" cy="12" r="12" fill="var(--green-bright)"/>
          <path d="M7,8 Q12,5 17,8 L16,10 H14 L13,9 H11 L10,10 H8 Z M8,12 H16 L17,17 H7 Z" fill="var(--card-black)"/>
        </svg>
        0400 555 018
      </li>
      <li class="contacts__item">
        <svg class="contacts__icon" viewBox="0 0 24 24" aria-hidden="true">
          <circle cx="12" cy="12" r="12" fill="var(--green-bright)"/>
          <rect x="6" y="8" width="12" height="8" fill="none" stroke="var(--card-black)" stroke-width="1.6"/>
          <path d="M6,8 L12,13 L18,8" fill="none" stroke="var(--card-black)" stroke-width="1.6"/>
        </svg>
        mara@copperwren.com
      </li>
      <li class="contacts__item">
        <svg class="contacts__icon" viewBox="0 0 24 24" aria-hidden="true">
          <circle cx="12" cy="12" r="12" fill="var(--green-bright)"/>
          <circle cx="12" cy="12" r="6.5" fill="none" stroke="var(--card-black)" stroke-width="1.4"/>
          <ellipse cx="12" cy="12" rx="2.8" ry="6.5" fill="none" stroke="var(--card-black)" stroke-width="1.2"/>
          <line x1="5.5" y1="12" x2="18.5" y2="12" stroke="var(--card-black)" stroke-width="1.2"/>
        </svg>
        www.copperwren.com
      </li>
    </ul>
  </article>
</body>
</html>
```